THE QUIET LEDGER - "Trade" size book cover design for a novel

THE QUIET LEDGER is a thriller that explores what happens at THE QUIET LEDGER life and death. I'd like to see a cover that reflects the near death experience scenes, but I am open to any creative cover that reflects the theme of the book and the sample scenes that I have attached. Please read the scenes.
Space should be left on the cover for the typical promotional text, etc.

NOVEL SUMMARY - Dr. Pelham Rudnick is skeptical of the afterlife. He doesn't believe he will be reunited with his wife, or joined with God in heaven. What he knows, or thinks he knows, is that he should have seen the warning signs of his wife's heart attack, should have saved her. After four years of mourning, Pelham is finally moving on, succumbing to lust and longing, instead of sorrow. Still he fears the little mistakes that can kill, like a missed diagnosis, or the slip of a scalpel -- the kind of mistakes that depression feeds. When he dates the mother of an epileptic patient, he begins to believe that death will finally stop controlling his life. He has no idea, that the woman of his desires has killed her first husband, and will soon kill her son. As Pelham falls in love and marries, he also becomes involved in a clinical study of near death experiences. Life and research are about to collide.

The designs I have seen so far are quite dark and seem like they would better fit a horror novel. I am looking for something that is more beautiful. The near death experience scenes in the book are hopeful and wonderous. I also would prefer not to have a dark tunnel representing near death. Moths can also be beautiful creatures. I attached scenes from the book in the original post that might be helpful.

You don't have to use the moth as the focal point, or you might want to use moths as they appear in the main near death scene. I am not wedded to that idea.

Here are some additional ideas for designs: 1. At the climax of the book, there is a scene (see attachment) where there is a fight, and the main character's wife tries to kill him. In that scene, the main character breaks a picture frame with a Hercules Moth specimen over his wife's head. Perhaps a design could incorporate broken glass on the floor with the moth, in whole or part. It could even have a woman's foot wearing and athletic or bicycle shoe stepping on the glass. 2. In the scene where the main character has a near death experience (see attachment), there are vivid surreal descriptions of what he sees, including fluttering moths, numbers and colors. There are also visions of other souls represented as points of light. If this can be represented kind of like a representation of curvatures in space time, all the better. 3. When the main character is a boy, he is slightly autistic and is mesmerized by counting the leaves within a forest tall trees. That could be one possibility for a background. 4. When the main character and wife or on a bicycle vacation in Tuscany, they come across a vineyard after it rains. At the end of one of the vineyard rows, there is a beautiful multicolor rose bush. With droplets of water clinging to the petals. Perhaps there can be reflections in the water drops of moths, or something else (even if it is just light.)

Target Market(s)

Book Readers - Thrillers, suspense, near death experiences, medical(neurology).

Colors

Designer to choose colors to be used in the design.

Requirements
Must have
• Creative design that fits the theme of book. It should not be too dark and brooding (it is not a horror story.) It also should not look like a romance cover.
Nice to have
• One or more of the following as reflected in the attached scenes - Moths, (including Hercules moth); a silhouette of a middle aged bald man perhaps floating in the clouds, shards of broken glass from the picture frame in the climatic scene (not tempered glass from a windshield), near death graphics (not a dark tunnel), time/space or theoretical inspired graphic , the feeling of being caught between two worlds, tree canopy with lots of leaves; enlarged crystaline snow flakes each incorporating a symbol (such a pi, a circle with concentric octagons --ancient method of calculating area of circle, representations or pictures of moths, the symbol for infinity, shards of broken glass, prime numbers, bubbles of color. I am also not opposed to other abstract ideas.
Should not have
• Dark tunnels to represent near death.
• Romance novel cover or overly romantic.
• Horror type novel.

```html
<!DOCTYPE html>
<html lang="en">
<head>
<meta charset="utf-8">
<title>The Quiet Ledger — Cover Wrap</title>
<link rel="stylesheet" href="https://fonts.googleapis.com/css2?family=Cinzel:wght@400&family=EB+Garamond:wght@400&display=swap">
<style>
  :root {
    --page-bg: #efefef;
    --cover-deep: #1b2250;
    --cover-mid: #3a3470;
    --cover-dawn: #6b4a86;
    --ink-light: #fbf7f0;
    --silver-top: #ffffff;
    --silver-bottom: #cfc6dc;
    --glow-white: #fffaf0;
    --glow-gold: #ffdca0;
    --glow-rose: #f08a8a;
    --glow-violet: #9a6cb4;
  }
  * { box-sizing: border-box; margin: 0; padding: 0; }
  html, body {
    width: 899px;
    height: 1200px;
    overflow: hidden;
    background: var(--page-bg);
  }
  .canvas {
    position: relative;
    width: 899px;
    height: 1200px;
  }
  .cover-wrap {
    position: absolute;
    left: 11px;
    top: 298px;
    width: 876px;
    height: 605px;
    background: linear-gradient(90deg, var(--cover-deep) 0%, var(--cover-mid) 55%, var(--cover-dawn) 100%);
    overflow: hidden;
  }

  /* Back cover */
  .back-cover {
    position: absolute;
    left: 0;
    top: 0;
    width: 405px;
    height: 100%;
  }
  .back-blurb {
    position: absolute;
    left: 31px;
    top: 44px;
    width: 345px;
    font-family: "EB Garamond", Georgia, serif;
    font-weight: 400;
    font-size: 13.4px;
    line-height: 16.8px;
    color: var(--ink-light);
    text-align: justify;
    hyphens: auto;
  }

  /* Spine */
  .spine {
    position: absolute;
    left: 405px;
    top: 0;
    width: 64px;
    height: 100%;
  }
  .spine-text {
    position: absolute;
    left: 50%;
    top: 61px;
    transform: translateX(-50%);
    writing-mode: vertical-rl;
    font-family: "Cinzel", Georgia, serif;
    font-weight: 400;
    color: var(--ink-light);
    white-space: nowrap;
  }
  .spine-title {
    font-size: 20px;
    letter-spacing: 1px;
  }
  .spine-author {
    font-size: 15px;
    letter-spacing: 6px;
    margin-top: 40px;
  }

  /* Front cover */
  .front-cover {
    position: absolute;
    left: 469px;
    top: 0;
    width: 407px;
    height: 100%;
  }
  .cover-art {
    position: absolute;
    left: -30px;
    top: 100px;
    width: 467px;
    height: 467px;
    border-radius: 50%;
    background:
      radial-gradient(circle at 50% 50%,
        var(--glow-white) 0%,
        var(--glow-white) 16%,
        var(--glow-gold) 28%,
        var(--glow-rose) 44%,
        var(--glow-violet) 58%,
        rgba(107, 74, 134, 0) 72%);
  }
  .title-block {
    position: absolute;
    left: 32px;
    top: 50px;
    width: 346px;
    font-family: "Cinzel", Georgia, serif;
    font-weight: 400;
    text-align: center;
  }
  .title-line-top {
    display: block;
    font-size: 46px;
    line-height: 48px;
    color: var(--ink-light);
    letter-spacing: 1px;
  }
  .title-rule {
    display: block;
    height: 2px;
    margin: 4px 0 8px;
    background: var(--ink-light);
  }
  .title-line-bottom {
    display: block;
    font-size: 60px;
    line-height: 60px;
    letter-spacing: 2px;
    background: linear-gradient(180deg, var(--silver-top) 15%, var(--silver-bottom) 95%);
    -webkit-background-clip: text;
    background-clip: text;
    color: transparent;
  }
  .author-name {
    position: absolute;
    left: 0;
    width: 100%;
    top: 498px;
    text-align: center;
    font-family: "Cinzel", Georgia, serif;
    font-weight: 400;
    font-size: 33px;
    letter-spacing: 9px;
    color: var(--ink-light);
  }
</style>
</head>
<body>
<div class="canvas">
  <div class="cover-wrap">

    <section class="back-cover">
      <p class="back-blurb">Dr. Pelham Rudnick is skeptical of the afterlife. He doesn't believe he will be reunited with his wife, or joined with God in heaven. What he knows, or thinks he knows, is that he should have seen the warning signs of his wife's heart attack, should have saved her. After four years of mourning, Pelham is finally moving on, succumbing to lust and longing, instead of sorrow. Still he fears the little mistakes that can kill, like a missed diagnosis, or the slip of a scalpel -- the kind of mistakes that depression feeds. When he dates the mother of an epileptic patient, he begins to believe that death will finally stop controlling his life. He has no idea, that the woman of his desires has killed her first husband, and will soon kill her son. As Pelham falls in love and marries, he also becomes involved in a clinical study of near death experiences. Life and research are about to collide.</p>
    </section>

    <section class="spine">
      <div class="spine-text">
        <span class="spine-title">THE QUIET LEDGER</span>
        <span class="spine-author">AUTHOR NAME</span>
      </div>
    </section>

    <section class="front-cover">
      <div class="cover-art" role="img" aria-label="Moth specimen resting in a radiant warm light that softens through gold and rose into a violet dawn sky"></div>
      <h1 class="title-block">
        <span class="title-line-top">THE QUIET</span>
        <span class="title-rule"></span>
        <span class="title-line-bottom">LEDGER</span>
      </h1>
      <p class="author-name">AUTHOR NAME</p>
    </section>

  </div>
</div>
</body>
</html>
```